Webpages for Tuomivaara Software Consulting

Needed: Webpage design.
Details:
One page site with good looking fonts and simple modern design. Logo would also be nice.
Page is for Software consulting company called: "Tuomivaara Software Consulting". Tuomivaara is my surname.
Pages should tell viewer that the company is reliable and its employees are hard-core professionals.
Company currently has one employee, that's me. So what I do is what this company does. I am software consultant. Basicly that means that I do Java/JavaEE/Web programming as subcontractor.
Here is more detail information about me.
SPECIALTIES
- Enterprise J2EE Application Programming and Architectures,
- Web development and
- Agile development.
I have over a decade of experience on designing and creating Java based web-services and applications to multiple interfaces. I also have plenty of experience about software architectures, design patterns and integration into third party systems. I’ve got good knowledge about agile software development and testing processes and I am experienced ScrumMaster and software project leader.
Target Market(s)
IT Businesses, Coding companies... Anyone who is buying coding as service.
Industry/Entity Type
Software
Look and feel

```html
<!DOCTYPE html>
<html lang="en">
<head>
<meta charset="utf-8">
<title>Tuomivaara Software Consulting</title>
<link rel="stylesheet" href="https://fonts.googleapis.com/css2?family=Arimo:wght@400;700&family=PT+Sans+Narrow:wght@400;700&family=Tinos:wght@400;700&display=swap">
<style>
  :root {
    --hero-bg: #e4e4e4;
    --page-bg: #f4f4f4;
    --footer-bg: #232323;
    --ink: #333333;
    --ink-soft: #6a6a6a;
    --rule: #d2d2d2;
    --brand-teal: #1a8f9e;
    --accent-blue: #1c9fc4;
    --accent-green: #2a9a2a;
    --btn-green-top: #3cb83c;
    --btn-green-bottom: #1d8a1d;
    --dark-circle: #262626;
    --field-bg: #d9d9d9;
    --footer-text: #bdbdbd;
  }
  * { box-sizing: border-box; margin: 0; padding: 0; }
  html, body { width: 745px; height: 1200px; overflow: hidden; }
  body { position: relative; background: var(--page-bg); font-family: "Arimo", Arial, sans-serif; color: var(--ink); }
  .abs { position: absolute; }
  h1, h2, h3 { font-weight: 400; }

  /* Hero */
  .hero { position: absolute; left: 0; top: 0; width: 745px; height: 402px; background: radial-gradient(ellipse at 50% 40%, #ececec, var(--hero-bg)); border-bottom: 1px solid #cfcfcf; }
  .brand { left: 70px; top: 34px; display: flex; align-items: center; gap: 7px; font-family: "Arimo", Arial, sans-serif; font-weight: 700; font-size: 14px; color: var(--brand-teal); white-space: nowrap; }
  .brand-mark { width: 12px; height: 12px; background: var(--brand-teal); }
  .social-dot { width: 18px; height: 18px; border-radius: 50%; background: #b5b5b5; top: 18px; }
  .main-nav { left: 0; top: 58px; width: 745px; font-family: "Tinos", Georgia, serif; font-size: 12px; color: var(--ink); }
  .main-nav span { position: absolute; white-space: nowrap; }
  .main-nav .current { color: var(--accent-green); }
  .nav-sep { width: 1px; height: 18px; background: #cfcfcf; top: 56px; }
  .hero-rule { left: 62px; top: 85px; width: 621px; height: 1px; background: var(--rule); }
  .headline { left: 0; width: 745px; top: 102px; text-align: center; font-family: "PT Sans Narrow", sans-serif; font-weight: 400; font-size: 33px; color: #6b6b6b; text-shadow: 0 2px 2px rgba(0,0,0,.25); padding-left: 36px; white-space: nowrap; }
  .specialties-title { left: 66px; top: 166px; font-family: "Tinos", Georgia, serif; font-weight: 700; font-size: 19px; color: var(--accent-blue); letter-spacing: .5px; }
  .spec-item { left: 64px; display: flex; align-items: center; gap: 8px; font-family: "Tinos", Georgia, serif; font-size: 13.5px; color: var(--ink); white-space: nowrap; }
  .spec-icon { width: 20px; height: 20px; border-radius: 50%; flex: none; }
  .btn-learn { left: 172px; top: 327px; width: 131px; height: 38px; border-radius: 3px; background: linear-gradient(var(--btn-green-top), var(--btn-green-bottom)); color: #fff; font-weight: 700; font-size: 16px; text-align: center; line-height: 38px; box-shadow: 0 2px 3px rgba(0,0,0,.3); }
  .hero-art { left: 452px; top: 160px; width: 232px; height: 206px; }

  /* Programming highlights */
  .skill { display: flex; align-items: center; gap: 10px; top: 440px; }
  .skill-num { width: 44px; height: 44px; border-radius: 50%; background: var(--dark-circle); color: #fff; font-family: "Tinos", Georgia, serif; font-size: 22px; text-align: center; line-height: 44px; }
  .skill-name { font-family: "Tinos", Georgia, serif; font-size: 22px; line-height: 22px; color: var(--ink); }
  .skill-sub { font-family: "Tinos", Georgia, serif; font-size: 13px; color: var(--ink-soft); letter-spacing: .5px; }
  .rule { height: 1px; background: var(--rule); }

  .section-title { font-family: "Tinos", Georgia, serif; font-weight: 400; font-size: 17px; color: var(--ink); letter-spacing: .5px; }
  .item-title { font-family: "Tinos", Georgia, serif; font-weight: 700; font-size: 10.5px; color: var(--accent-green); line-height: 15px; }
  .item-body { font-size: 9.5px; line-height: 16px; color: var(--ink-soft); }
  .arrow { color: var(--accent-green); font-size: 7px; }
  .service-icon { left: 63px; width: 56px; height: 56px; border-radius: 6px; }
  .btn-small { height: 19px; border-radius: 2px; background: linear-gradient(var(--btn-green-top), var(--btn-green-bottom)); color: #fff; font-size: 8.5px; font-weight: 700; text-align: center; line-height: 19px; }
  .link-green { font-size: 9.5px; font-weight: 700; color: var(--accent-green); text-decoration: underline; }

  /* Footer */
  .footer { position: absolute; left: 0; top: 917px; width: 745px; height: 283px; background: var(--footer-bg); }
  .footer-edge { left: 0; top: 910px; width: 745px; height: 8px; }
  .contact-title { left: 63px; top: 938px; font-family: "PT Sans Narrow", sans-serif; font-weight: 700; font-size: 21px; color: var(--accent-blue); }
  .field { background: linear-gradient(#e6e6e6, var(--field-bg)); border-radius: 2px; font-size: 9px; color: #555; padding: 6px 10px; }
  .footer-rule { left: 62px; top: 1087px; width: 621px; height: 1px; background: #3a3a3a; }
  .footer-nav { left: 0; width: 745px; top: 1108px; text-align: center; font-family: "Tinos", Georgia, serif; font-size: 10.5px; color: var(--footer-text); word-spacing: 2px; }
  .footer-nav .current { color: var(--accent-green); }
  .footer-nav .sep { margin: 0 12px; }
  .copyright { left: 0; width: 745px; text-align: center; font-family: "Tinos", Georgia, serif; font-size: 10px; color: var(--footer-text); }
  .follow { left: 0; width: 745px; top: 1174px; display: flex; justify-content: center; align-items: center; gap: 8px; font-family: "Tinos", Georgia, serif; font-size: 10px; color: var(--footer-text); }
  .follow-dot { width: 15px; height: 15px; border-radius: 3px; background: #4a86c5; }
</style>
</head>
<body>

<header class="hero">
  <div class="abs brand"><span class="brand-mark"></span>Tuomivaara Software Consulting</div>
  <span class="abs social-dot" style="left:635px"></span>
  <span class="abs social-dot" style="left:663px"></span>

  <nav class="abs main-nav">
    <span class="current" style="left:309px">Home</span>
    <span style="left:370px">About Us</span>
    <span style="left:447px">Services</span>
    <span style="left:518px">Work</span>
    <span style="left:578px">Blog</span>
    <span style="left:631px">Contact Us</span>
  </nav>
  <span class="abs nav-sep" style="left:353px"></span>
  <span class="abs nav-sep" style="left:430px"></span>
  <span class="abs nav-sep" style="left:501px"></span>
  <span class="abs nav-sep" style="left:560px"></span>
  <span class="abs nav-sep" style="left:613px"></span>
  <div class="abs hero-rule"></div>

  <h1 class="abs headline">We are reliable and hard-core professionals.</h1>

  <h2 class="abs specialties-title">SPECIALTIES</h2>
  <div class="abs spec-item" style="top:204px"><span class="spec-icon" role="img" aria-label="Small gear icon" style="background:radial-gradient(#f0f0f0,#9a9a9a)"></span>Enterprise J2EE Application Programming and Architectures,</div>
  <div class="abs spec-item" style="top:234px"><span class="spec-icon" role="img" aria-label="Small globe icon" style="background:radial-gradient(#e8f3c8,#7aa63a)"></span>Web development</div>
  <div class="abs spec-item" style="top:264px"><span class="spec-icon" role="img" aria-label="Small agile process icon" style="background:radial-gradient(#bfe3f7,#2a7fbf)"></span>Agile development.</div>

  <div class="abs btn-learn">Learn More</div>

  <div class="abs hero-art" role="img" aria-label="Tablet showing a rising blue bar chart with a golden arrow" style="background:linear-gradient(160deg,#e4e4e4 0%,#bcd3ea 35%,#2f7fd0 60%,#222 85%,#e4e4e4 100%);border-radius:14px"></div>
</header>

<main>
  <div class="abs skill" style="left:63px"><span class="skill-num">01</span><div><div class="skill-name">JAVA</div><div class="skill-sub">PROGRAMMING</div></div></div>
  <div class="abs skill" style="left:297px"><span class="skill-num">02</span><div><div class="skill-name">JAVAEE</div><div class="skill-sub">PROGRAMMING</div></div></div>
  <div class="abs skill" style="left:528px"><span class="skill-num">03</span><div><div class="skill-name">WEB</div><div class="skill-sub">PROGRAMMING</div></div></div>
  <div class="abs rule" style="left:62px;top:511px;width:621px"></div>

  <!-- Services -->
  <h3 class="abs section-title" style="left:64px;top:541px">OUR &nbsp;SERVICES</h3>
  <div class="abs rule" style="left:62px;top:570px;width:386px"></div>

  <div class="abs service-icon" role="img" aria-label="Design document and pencil illustration" style="top:594px;background:linear-gradient(135deg,#cfe6f7,#3a8fd0)"></div>
  <div class="abs" style="left:141px;top:591px;width:300px">
    <div class="item-title">LOREM IPSUM DOLOR SIT AMET CONSE</div>
    <p class="item-body" style="margin-top:6px">Lorem ipsum dolor sit amet conse ctetur adipisicing elit, sed do incididunt ut labore et dolore magna aliqua. Ut enim ad minim quis nostrud exercitation ullamco laboris nisi ut aliquip. <span class="arrow">&#9654;</span></p>
  </div>

  <div class="abs service-icon" role="img" aria-label="Folder with documents illustration" style="top:681px;background:linear-gradient(135deg,#f2deb0,#b98a3a)"></div>
  <div class="abs" style="left:141px;top:678px;width:300px">
    <div class="item-title">LOREM IPSUM DOLOR SIT AMET CONSE</div>
    <p class="item-body" style="margin-top:6px">Lorem ipsum dolor sit amet conse ctetur adipisicing elit, sed do incididunt ut labore et dolore magna aliqua. Ut enim ad minim quis nostrud exercitation ullamco laboris nisi ut aliquip. <span class="arrow">&#9654;</span></p>
  </div>

  <div class="abs service-icon" role="img" aria-label="Green gear illustration" style="top:768px;background:radial-gradient(#9fe07a,#3f9a1e);border-radius:50%"></div>
  <div class="abs" style="left:141px;top:765px;width:300px">
    <div class="item-title">LOREM IPSUM DOLOR SIT AMET CONSE</div>
    <p class="item-body" style="margin-top:6px">Lorem ipsum dolor sit amet conse ctetur adipisicing elit, sed do incididunt ut labore et dolore magna aliqua. Ut enim ad minim quis nostrud exercitation ullamco laboris nisi ut aliquip. <span class="arrow">&#9654;</span></p>
  </div>

  <div class="abs rule" style="left:62px;top:853px;width:386px"></div>
  <div class="abs btn-small" style="left:63px;top:867px;width:73px">See all services</div>

  <!-- About -->
  <h3 class="abs section-title" style="left:475px;top:541px">ABOUT &nbsp;US</h3>
  <div class="abs rule" style="left:472px;top:570px;width:211px"></div>
  <div class="abs" style="left:473px;top:591px;width:212px">
    <div class="item-title">LOREM IPSUM DOLOR SIT AMET CONSE CTETUR ADIPISICING ELIT</div>
    <p class="item-body" style="margin-top:8px">Lorem ipsum dolor sit amet conse ctetur elit, sed do tempo incididunt ut labore et dolore magna aliqua. Ut enim ad minim veniam,quis nostrud exercitation ullamco laboris nisi ut aliquip. <span class="arrow">&#9654;</span></p>
  </div>

  <h3 class="abs section-title" style="left:475px;top:725px">TESTIMONIALS</h3>
  <div class="abs rule" style="left:472px;top:752px;width:211px"></div>
  <p class="abs item-body" style="left:473px;top:771px;width:212px">Lorem ipsum dolor sit amet conse ctetur elit, sed do tempo incididunt ut labore et dolore magna aliqua.</p>
  <div class="abs" role="img" aria-label="Client avatar" style="left:564px;top:828px;width:16px;height:16px;border-radius:50%;background:linear-gradient(#e8b08a,#c0392b)"></div>
  <div class="abs" style="left:590px;top:826px;font-size:8px;line-height:11px;white-space:nowrap">
    <div style="font-weight:700;color:var(--ink)">Lorem ipsum dolo</div>
    <div style="color:var(--ink-soft)">Dolor sit amet conse ctetur</div>
  </div>
  <div class="abs rule" style="left:472px;top:853px;width:211px"></div>
  <span class="abs link-green" style="left:473px;top:875px">See all</span>
</main>

<svg class="abs footer-edge" viewBox="0 0 745 8" preserveAspectRatio="none" aria-hidden="true">
  <polygon fill="#232323" points="0,8 0,4 745,4 745,8"/>
</svg>
<footer class="footer"></footer>

<h2 class="abs contact-title">GET IN TOUCH</h2>
<div class="abs field" style="left:63px;top:974px;width:181px;height:22px">Name:</div>
<div class="abs field" style="left:63px;top:1012px;width:181px;height:22px">E-mail:</div>
<div class="abs field" style="left:264px;top:974px;width:419px;height:59px">Comments:</div>
<div class="abs btn-small" style="left:63px;top:1048px;width:39px">Send</div>
<div class="abs btn-small" style="left:109px;top:1048px;width:39px">Reset</div>

<div class="abs footer-rule"></div>
<nav class="abs footer-nav">
  <span class="current">Home</span><span class="sep">|</span>About Us<span class="sep">|</span>Services<span class="sep">|</span>Work<span class="sep">|</span>Blog<span class="sep">|</span>Contact Us
</nav>
<p class="abs copyright" style="top:1136px">© Copyright 2011 Tuomivaara Software Consulting. All Rights Reserved</p>
<p class="abs copyright" style="top:1153px">Website Design &amp; Developed &nbsp;| SEO PPC Services : www.northpixelstudio.com</p>
<div class="abs follow">Follow Us on : <span class="follow-dot"></span><span class="follow-dot" style="background:#3b5a9a"></span></div>

</body>
</html>
```